Mentoring children in Education for early success

We are seeking a PowerPoint that illustrates how a nationwide mentoring system can reduce the educational disparity among low income children. We would like to illustrate a design that represents a national effort (map of Us)--a learning laboratory where children are educated in using computers in their communities.

The scope of work consist of 18 slides, but for the initial entries I Iike to see the cover page and 2 inner slides with text.

Please see the content in the attachments.

Target Market(s)

Social Service program practioners

Industry/Entity Type

Education

Font styles to use
Sans Serif

Requirements
Must have
• Illustrations
Nice to have
• Map of Us
• Illustration of School House
• Illustration of Children at computer stations

```html
<!DOCTYPE html>
<html lang="en">
<head>
<meta charset="utf-8">
<title>Who Are These Children</title>
<link rel="stylesheet" href="https://fonts.googleapis.com/css2?family=Carlito:wght@400;700&family=Arimo:wght@400;700&display=swap">
<style>
  :root {
    --page-bg: #ffffff;
    --title-blue: #4a86d0;
    --bar-above: #4f4a9f;
    --bar-below: #fbb918;
    --ink: #231f20;
    --axis-ink: #3a3a3a;
    --grid: #9a9a9a;
  }
  html, body {
    margin: 0;
    padding: 0;
    width: 1200px;
    height: 960px;
    overflow: hidden;
    background: var(--page-bg);
  }
  .slide {
    position: relative;
    width: 1200px;
    height: 960px;
  }
  .slide-title {
    position: absolute;
    top: 88px;
    left: 0;
    width: 1138px;
    margin: 0;
    text-align: center;
    font-family: "Carlito", "Calibri", sans-serif;
    font-weight: 700;
    font-size: 35px;
    color: var(--title-blue);
    text-decoration: underline;
    text-decoration-thickness: 2px;
    text-underline-offset: 4px;
  }
  .chart {
    position: absolute;
    top: 0;
    left: 0;
  }
  .chart text {
    font-family: "Arimo", "Arial", sans-serif;
    fill: var(--axis-ink);
  }
  .chart .chart-heading { font-size: 15.5px; font-weight: 700; fill: var(--ink); }
  .chart .tick-label { font-size: 14px; }
  .chart .axis-title { font-size: 12px; letter-spacing: 1px; }
  .chart .category-label { font-size: 13.5px; }
  .chart .legend-label { font-size: 12px; letter-spacing: 0.3px; }
  .chart .source-note { font-size: 11px; fill: var(--ink); }
  .gridline { stroke: var(--grid); stroke-width: 1; }
  .plot-frame { fill: none; stroke: var(--grid); stroke-width: 1; }
  .bar-above { fill: var(--bar-above); }
  .bar-below { fill: var(--bar-below); }
</style>
</head>
<body>
<main class="slide">
  <h1 class="slide-title">Who Are These Children</h1>

  <svg class="chart" width="1200" height="960" viewBox="0 0 1280 1024" role="img" aria-label="Bar chart: percentage of children ages 3 to 6 with selected school readiness skills, by poverty status">
    <g class="chart-title">
      <text class="chart-heading" x="484" y="234">Percentage of Children Ages 3–6</text>
      <text class="chart-heading" x="484" y="257">With Selected School Readiness Skills,</text>
      <text class="chart-heading" x="484" y="280">by Poverty Status</text>
    </g>

    <g class="grid">
      <line class="gridline" x1="483" y1="716" x2="835" y2="716"/>
      <line class="gridline" x1="483" y1="672" x2="835" y2="672"/>
      <line class="gridline" x1="483" y1="628" x2="835" y2="628"/>
      <line class="gridline" x1="483" y1="584" x2="835" y2="584"/>
      <line class="gridline" x1="483" y1="540" x2="835" y2="540"/>
      <line class="gridline" x1="483" y1="496" x2="835" y2="496"/>
      <line class="gridline" x1="483" y1="452" x2="835" y2="452"/>
      <line class="gridline" x1="483" y1="408" x2="835" y2="408"/>
      <line class="gridline" x1="483" y1="364" x2="835" y2="364"/>
      <rect class="plot-frame" x="483" y="320" width="352" height="440"/>
    </g>

    <g class="y-axis" text-anchor="end">
      <text class="tick-label" x="479" y="765">0</text>
      <text class="tick-label" x="479" y="721">10</text>
      <text class="tick-label" x="479" y="677">20</text>
      <text class="tick-label" x="479" y="633">30</text>
      <text class="tick-label" x="479" y="589">40</text>
      <text class="tick-label" x="479" y="545">50</text>
      <text class="tick-label" x="479" y="501">60</text>
      <text class="tick-label" x="479" y="457">70</text>
      <text class="tick-label" x="479" y="413">80</text>
      <text class="tick-label" x="479" y="369">90</text>
      <text class="tick-label" x="479" y="325">100</text>
      <text class="axis-title" transform="translate(445 542) rotate(-90)" text-anchor="middle">PERCENT</text>
    </g>

    <g class="legend">
      <rect class="bar-above" x="664" y="345" width="11" height="11"/>
      <text class="legend-label" x="680" y="355">above poverty threshold</text>
      <rect class="bar-below" x="664" y="372" width="11" height="11"/>
      <text class="legend-label" x="680" y="382">below poverty threshold</text>
    </g>

    <g class="bars">
      <rect class="bar-above" x="512" y="606" width="15" height="154"/>
      <rect class="bar-below" x="541" y="667.6" width="15" height="92.4"/>
      <rect class="bar-above" x="598" y="465.2" width="15" height="294.8"/>
      <rect class="bar-below" x="627" y="544.4" width="15" height="215.6"/>
      <rect class="bar-above" x="684" y="478.4" width="15" height="281.6"/>
      <rect class="bar-below" x="713" y="557.6" width="15" height="202.4"/>
      <rect class="bar-above" x="770" y="720.4" width="15" height="39.6"/>
      <rect class="bar-below" x="799" y="733.6" width="15" height="26.4"/>
    </g>

    <g class="x-axis" text-anchor="middle">
      <text class="category-label" x="531" y="790">Recognizes</text>
      <text class="category-label" x="529" y="807">all letters</text>
      <text class="category-label" x="622" y="790">Counts to 20</text>
      <text class="category-label" x="620" y="807">or higher</text>
      <text class="category-label" x="705" y="790">Writes</text>
      <text class="category-label" x="705" y="807">name</text>
      <text class="category-label" x="791" y="790">Reads words</text>
      <text class="category-label" x="791" y="807">in a book</text>
      <text class="axis-title" x="663" y="841">SELECTED SCHOOL READINESS SKILLS</text>
    </g>

    <g class="source">
      <text class="source-note" x="484" y="887">Source: Marlowe, Dana. Parents’ Reports of the School Readiness</text>
      <text class="source-note" x="484" y="903">of Young Children from the National Family Learning Surveys</text>
      <text class="source-note" x="484" y="919">Program of 2007, Table 2. National Bureau for Learning Data.</text>
      <text class="source-note" x="484" y="936">August 2008. www.kidsreadydata.org/?q=node/291</text>
    </g>
  </svg>
</main>
</body>
</html>
```